Re-Design an adult education portal

I need support to re-design an adult education portal. Currently the customer has an incomplete website which should be prepared in a new format.
I have the idea how to realize, but I have no clue how to design it. The hard thing is to have a "beautiful" website with available logo and main color. I hope you can support me.

Name of Website: tovrenu (tovrenu.ch)
Content: adult eduction for adult in safety at work, mountain climbing, dog school. various courses in different areas. But on old webpage is hard to find the different possibilities.
main color: Ral 6011 (green) -> #6C7C59
logo: you see on top of website the logo (2 dogs and a mountain with a colour gradient).

new website: for new webpage I decided to have a navigation for each section of education. In the main area I would like to have some pictures to give an idea what content is behind. At the moment it looks terrible, so I decided to use you as support for me to make the webpage prettier :). And maybe you have an better idea how to make it great. -> current state of new web page: https://tovrenu.bask-om.ch/

Target Market(s)

adult eduction for adult in safety at work, mountain climbing, dog school

Number of Pages Required

1 page

Font styles to use
Serif
Sans Serif

Requirements
Must have
• As main color is set "Ral 6011" (green) -> #6C7C59

```html
<!DOCTYPE html>
<html lang="en">
<head>
<meta charset="utf-8">
<title>tovrenu – Adult Education</title>
<link href="https://fonts.googleapis.com/css2?family=Jost:wght@300;400;500;600&display=swap" rel="stylesheet">
<style>
:root{
  --green:#6C7C59;
  --green-dark:#5a6849;
  --ink:#222222;
  --text:#555555;
  --light:#f4f4f4;
  --white:#ffffff;
  --line:#dddddd;
}
*{box-sizing:border-box;margin:0;padding:0}
html,body{width:1200px;height:4800px;overflow:hidden}
body{position:relative;font-family:'Jost',sans-serif;color:var(--text);background:var(--white)}
.abs{position:absolute}
.btn{display:inline-block;border-radius:20px;font-size:10px;font-weight:600;letter-spacing:.5px;text-transform:uppercase;color:#fff;text-align:center}
.btn-green{background:var(--green)}
.btn-dark{background:var(--ink)}
.eyebrow{font-size:11px;text-transform:uppercase;color:var(--ink);letter-spacing:.3px}
.h2{font-size:28px;font-weight:400;color:var(--green);line-height:1.3}
.body{font-size:12px;line-height:2;color:var(--text)}
.center{text-align:center}

/* top bar */
.topbar{left:0;top:0;width:1200px;height:47px;background:var(--ink);color:#ddd;font-size:11px}
.topbar span{position:absolute;top:16px}
.social-tab{left:903px;top:0;width:297px;height:47px;background:var(--green);border-radius:24px 0 0 24px}
.social-tab i{position:absolute;top:17px;width:12px;height:12px;border:1.5px solid #dfe5d6;border-radius:50%}

/* nav */
.nav{left:0;top:47px;width:1200px;height:65px;background:#fff;border-bottom:1px solid #eee}
.logo{font-size:22px;font-weight:500;color:var(--green)}
.nav-links span{position:absolute;top:26px;font-size:11px;color:var(--ink);font-weight:500}

/* hero */
.hero{left:0;top:112px;width:1200px;height:428px;background:linear-gradient(180deg,#7d8a99 0%,#a9b3bd 45%,#cfd3d6 100%)}
.hero-figure{left:210px;top:50px;width:130px;height:378px;background:linear-gradient(180deg,#4a4d4f,#2c2e2f);opacity:.35;border-radius:60px 60px 0 0}
.hero-text{left:300px;top:105px;width:600px;text-align:center;color:#fff}
.hero-text h1{font-size:32px;font-weight:300;line-height:1.4}
.hero-text b{font-weight:500}
.arrow-circle{width:40px;height:40px;border-radius:50%;border:1.5px solid #fff}
</style>
</head>
<body>

<!-- top bar -->
<div class="abs topbar">
  <span style="left:162px">
    <svg width="11" height="11" viewBox="0 0 12 12" style="vertical-align:-1px;margin-right:10px"><rect x="1" y="2" width="10" height="7" fill="none" stroke="#ddd" stroke-width="1.2"/></svg>Are you interested in Life Coaching
  </span>
  <span style="left:633px">
    <svg width="12" height="10" viewBox="0 0 12 10" style="vertical-align:-1px;margin-right:6px"><rect x="1" y="1" width="10" height="8" fill="none" stroke="#ddd"/><path d="M1 1l5 4 5-4" fill="none" stroke="#ddd"/></svg>info@tovrenu.ch
  </span>
  <span style="left:755px">
    <svg width="8" height="12" viewBox="0 0 8 12" style="vertical-align:-1px;margin-right:8px"><rect x="1" y="1" width="6" height="10" rx="1" fill="none" stroke="#ddd"/></svg>+41 79 512 80 47
  </span>
</div>
<div class="abs social-tab">
  <i style="left:48px"></i><i style="left:74px"></i><i style="left:100px"></i><i style="left:126px"></i>
</div>

<!-- nav -->
<div class="abs nav">
  <div class="abs logo" style="left:162px;top:16px">tovrenu.ch</div>
  <div class="nav-links">
    <span style="left:296px">Home</span>
    <span style="left:347px">Occupational safety ⌄</span>
    <span style="left:472px">First Aid ⌄</span>
    <span style="left:546px">Dog School ⌄</span>
    <span style="left:635px">CZV ⌄</span>
    <span style="left:690px">Mountain Training ⌄</span>
    <span style="left:807px">About tovrenu ⌄</span>
  </div>
  <div class="abs btn btn-dark" style="left:898px;top:13px;width:140px;height:39px;line-height:39px;font-size:9px">Learn course now!</div>
</div>

<!-- hero -->
<div class="abs hero" role="img" aria-label="Photo of a child standing on a tall ladder reaching into a cloudy sky">
  <div class="abs hero-figure"></div>
  <div class="abs hero-text">
    <div style="font-size:10px;letter-spacing:.4px;margin-bottom:12px">YOUR TRAINING AND COURSE PARTNER</div>
    <h1>We offer <b>training tailored</b> to your<br><b>needs,</b> target-oriented and tailored<br>to <b>your skills</b> and knowledge.</h1>
    <div class="btn btn-dark" style="margin-top:18px;width:126px;height:34px;line-height:34px;font-size:9px">Learn course now!</div>
  </div>
  <div class="abs arrow-circle" style="left:24px;top:195px"><svg width="40" height="40"><path d="M22 14l-6 6 6 6" fill="none" stroke="#fff" stroke-width="1.5"/></svg></div>
  <div class="abs arrow-circle" style="left:1138px;top:195px;background:var(--green);border-color:var(--green)"><svg width="40" height="40"><path d="M18 14l6 6-6 6" fill="none" stroke="#fff" stroke-width="1.5"/></svg></div>
</div>

<!-- who we are -->
<div class="abs" style="left:0;top:540px;width:1200px;height:634px;background:var(--light)">
  <svg class="abs" style="left:162px;top:93px" width="498" height="451" viewBox="0 0 498 451">
    <path d="M0 400 L498 340 L498 380 L0 451 Z" fill="var(--green)"/>
  </svg>
  <div class="abs" role="img" aria-label="Photo of a hiker with a camera looking at snowy mountains" style="left:162px;top:93px;width:498px;height:414px;background:linear-gradient(135deg,#e4e8ec 0%,#9aa6ad 50%,#46505a 100%);clip-path:polygon(0 0,100% 0,100% 88%,0 100%)"></div>
  <div class="abs" style="left:690px;top:100px;width:348px">
    <div class="eyebrow">Who we are</div>
    <div class="h2" style="font-size:25px;margin-top:14px;letter-spacing:.5px">Lorem ipsum dolor sit amet, consectetur adipiscing.</div>
    <p class="body" style="margin-top:20px;text-align:justify">Lorem ipsum dolor sit amet, consectetur adipiscing elit. Etiam sollicitudin ante in purus viverra, vitae tempor lorem laoreet. Vestibulum feugiat, ipsum a euismod finibus, massa nisl tristique lacus, eget pellentesque urna metus a turpis. Nullam eget feugiat enim.</p>
    <p class="body" style="margin-top:20px;text-align:justify">Lorem ipsum dolor sit amet, consectetur adipiscing elit. Etiam sollicitudin ante in purus viverra, vitae tempor lorem laoreet. Vestibulum feugiat, ipsum a euismod finibus, massa nisl tristique lacus, eget pellentesque urna metus a turpis.</p>
  </div>
  <div class="abs btn btn-dark" style="left:692px;top:465px;width:114px;height:34px;line-height:34px;font-size:9px">Read more</div>
  <div class="abs" style="left:838px;top:462px">
    <div style="font-size:11px;color:var(--ink)">CALL TO ASK ANY QUESTION</div>
    <div style="font-size:24px;color:var(--green);line-height:1.1">+41 79 512 80 47</div>
  </div>
</div>

<!-- courses -->
<div class="abs" style="left:0;top:1174px;width:1200px;height:674px;background:#fff">
  <div class="abs center" style="left:0;top:92px;width:1200px">
    <div class="eyebrow">Our courses</div>
    <div class="h2" style="margin-top:6px">Explore How can We help you</div>
    <p class="body" style="margin-top:6px">Lorem ipsum dolor sit amet, consectetur adipiscing elit. Etiam<br>sollicitudin ante in purus viverra, vitae tempor lorem laoreet.</p>
  </div>
  <svg class="abs" style="left:92px;top:372px" width="26" height="40"><path d="M20 2L4 20l16 18" fill="none" stroke="#333" stroke-width="2"/></svg>
  <svg class="abs" style="left:1082px;top:372px" width="26" height="40"><path d="M6 2l16 18L6 38" fill="none" stroke="#333" stroke-width="2"/></svg>
</div>

<!-- course cards -->
<div class="abs" style="left:162px;top:1493px;width:274px;height:258px;background:#fff;border:1px solid #e5e5e5;border-radius:4px"></div>
<div class="abs" style="left:464px;top:1493px;width:274px;height:258px;background:var(--green);border-radius:4px"></div>
<div class="abs" style="left:766px;top:1493px;width:274px;height:258px;background:#fff;border:1px solid #e5e5e5;border-radius:4px"></div>

<div class="abs" role="img" aria-label="Photo of a red forklift in a warehouse" style="left:176px;top:1407px;width:240px;height:162px;background:linear-gradient(180deg,#c9cbcc,#8c9092)"></div>
<div class="abs" role="img" aria-label="Photo of a red forklift in a warehouse" style="left:480px;top:1407px;width:240px;height:162px;background:linear-gradient(180deg,#c9cbcc,#8c9092)"></div>
<div class="abs" role="img" aria-label="Photo of a red forklift in a warehouse" style="left:782px;top:1407px;width:240px;height:162px;background:linear-gradient(180deg,#c9cbcc,#8c9092)"></div>

<!-- card icons -->
<div class="abs" style="left:270px;top:1540px;width:56px;height:56px;border-radius:50%;background:#fff;border:2px solid var(--green)"><svg width="52" height="52" viewBox="0 0 52 52"><rect x="16" y="14" width="20" height="10" fill="none" stroke="var(--green)" stroke-width="1.5"/><circle cx="18" cy="30" r="2.5" fill="none" stroke="var(--green)"/><circle cx="24" cy="30" r="2.5" fill="none" stroke="var(--green)"/><circle cx="30" cy="30" r="2.5" fill="none" stroke="var(--green)"/><circle cx="36" cy="30" r="2.5" fill="none" stroke="var(--green)"/><path d="M15 40v-5h6v5M21 40v-5h6v5M27 40v-5h6v5M33 40v-5h6v5" fill="none" stroke="var(--green)"/></svg></div>
<div class="abs" style="left:572px;top:1540px;width:56px;height:56px;border-radius:50%;background:var(--green);border:2px solid #fff"><svg width="52" height="52" viewBox="0 0 52 52"><rect x="16" y="14" width="20" height="10" fill="none" stroke="#fff" stroke-width="1.5"/><circle cx="18" cy="30" r="2.5" fill="none" stroke="#fff"/><circle cx="24" cy="30" r="2.5" fill="none" stroke="#fff"/><circle cx="30" cy="30" r="2.5" fill="none" stroke="#fff"/><circle cx="36" cy="30" r="2.5" fill="none" stroke="#fff"/><path d="M15 40v-5h6v5M21 40v-5h6v5M27 40v-5h6v5M33 40v-5h6v5" fill="none" stroke="#fff"/></svg></div>
<div class="abs" style="left:874px;top:1540px;width:56px;height:56px;border-radius:50%;background:#fff;border:2px solid var(--green)"><svg width="52" height="52" viewBox="0 0 52 52"><rect x="16" y="14" width="20" height="10" fill="none" stroke="var(--green)" stroke-width="1.5"/><circle cx="18" cy="30" r="2.5" fill="none" stroke="var(--green)"/><circle cx="24" cy="30" r="2.5" fill="none" stroke="var(--green)"/><circle cx="30" cy="30" r="2.5" fill="none" stroke="var(--green)"/><circle cx="36" cy="30" r="2.5" fill="none" stroke="var(--green)"/><path d="M15 40v-5h6v5M21 40v-5h6v5M27 40v-5h6v5M33 40v-5h6v5" fill="none" stroke="var(--green)"/></svg></div>

<div class="abs center" style="left:162px;top:1614px;width:274px">
  <div style="font-size:16px;color:var(--ink);line-height:1.35">Lorem ipsum dolor sit amet,<br>consectetur adipiscing elit</div>
  <p style="font-size:11px;line-height:1.7;margin-top:10px">Nunc aliquet nulla nec dapibus max imus.<br>Nam aliquam neque.</p>
</div>
<div class="abs center" style="left:464px;top:1614px;width:274px;color:#fff">
  <div style="font-size:16px;line-height:1.35">Lorem ipsum dolor sit amet,<br>consectetur adipiscing elit</div>
  <p style="font-size:11px;line-height:1.7;margin-top:10px">Nunc aliquet nulla nec dapibus max imus.<br>Nam aliquam neque.</p>
</div>
<div class="abs center" style="left:766px;top:1614px;width:274px">
  <div style="font-size:16px;color:var(--ink);line-height:1.35">Lorem ipsum dolor sit amet,<br>consectetur adipiscing elit</div>
  <p style="font-size:11px;line-height:1.7;margin-top:10px">Nunc aliquet nulla nec dapibus max imus.<br>Nam aliquam neque.</p>
</div>
<div class="abs btn btn-green" style="left:234px;top:1733px;width:128px;height:34px;line-height:34px;font-size:9px">Get here</div>
<div class="abs btn btn-dark" style="left:536px;top:1733px;width:128px;height:34px;line-height:34px;font-size:9px">Get here</div>
<div class="abs btn btn-green" style="left:838px;top:1733px;width:128px;height:34px;line-height:34px;font-size:9px">Get here</div>

<!-- health specialist -->
<div class="abs" role="img" aria-label="Photo of a hiker with a backpack standing on a rock above misty valleys" style="left:0;top:1848px;width:604px;height:563px;background:linear-gradient(180deg,#3b3f44 0%,#6f757a 55%,#b9bbbb 100%)"></div>
<div class="abs" style="left:604px;top:1848px;width:596px;height:563px;background:var(--light)">
  <div class="abs" style="left:32px;top:78px;width:530px">
    <div class="eyebrow">Health specialist</div>
    <div class="h2" style="margin-top:8px">Lorem ipsum dolor sit amet, consectetur adipiscing elit. tempor lorem laoreet.</div>
    <p class="body" style="margin-top:18px">Lorem ipsum dolor sit amet, consectetur adipiscing elit. Etiam sollicitudin ante in purus viverra, vitae tempor lorem laoreet. Vestibulum feugiat, ipsum a euismod finibus, massa nisl tristique lacus, eget pellentesque urna metus a turpis. Nullam eget feugiat enim. Sed id finibus felis. Quisque tincidunt nisl vel risus dapibus, sit amet aliquet justo elementum. Nam non lectus nisi. Nullam eget risus neque.</p>
    <p class="body" style="margin-top:18px">Lorem ipsum dolor sit amet, consectetur adipiscing elit. Etiam sollicitudin ante in purus viverra, vitae tempor lorem laoreet. Vestibulum feugiat, ipsum a euismod finibus, massa nisl tristique lacus, eget pellentesque urna metus a turpis.</p>
  </div>
  <div class="abs btn btn-green" style="left:32px;top:442px;width:128px;height:34px;line-height:34px;font-size:9px">Read more</div>
</div>

<!-- dog school -->
<div class="abs" style="left:0;top:2411px;width:611px;height:560px;background:var(--light)">
  <div class="abs" style="left:71px;top:78px;width:520px">
    <div class="eyebrow">Dog school</div>
    <div class="h2" style="margin-top:8px">Lorem ipsum dolor sit amet, consectetur adipiscing elit. tempor lorem laoreet.</div>
    <p class="body" style="margin-top:18px">Lorem ipsum dolor sit amet, consectetur adipiscing elit. Etiam sollicitudin ante in purus viverra, vitae tempor lorem laoreet. Vestibulum feugiat, ipsum a euismod finibus, massa nisl tristique lacus, eget pellentesque urna metus a turpis. Nullam eget feugiat enim. Sed id finibus felis. Quisque tincidunt nisl vel risus dapibus, sit amet aliquet justo elementum. Nam non lectus nisi. Nullam eget risus neque.</p>
    <p class="body" style="margin-top:18px">Lorem ipsum dolor sit amet, consectetur adipiscing elit. Etiam sollicitudin ante in purus viverra, vitae tempor lorem laoreet. Vestibulum feugiat, ipsum a euismod finibus, massa nisl tristique lacus, eget pellentesque urna metus a turpis.</p>
  </div>
  <div class="abs btn btn-green" style="left:71px;top:442px;width:128px;height:34px;line-height:34px;font-size:9px">Read more</div>
</div>
<div class="abs" role="img" aria-label="Photo of a brown dog with a red collar sitting in a car" style="left:611px;top:2411px;width:589px;height:560px;background:radial-gradient(ellipse at 55% 45%,#8a4a2c 0%,#4a2a1c 35%,#14181d 75%)"></div>

<!-- center icon box -->
<div class="abs" style="left:546px;top:2357px;width:108px;height:108px;background:#fff;border-radius:14px;box-shadow:0 4px 14px rgba(0,0,0,.12)">
  <svg width="108" height="108" viewBox="0 0 108 108"><rect x="32" y="24" width="44" height="22" fill="none" stroke="var(--green)" stroke-width="2.5"/><path d="M38 32h30M38 38h20" stroke="var(--green)" stroke-width="2"/><circle cx="36" cy="58" r="5" fill="none" stroke="var(--green)" stroke-width="2"/><circle cx="49" cy="58" r="5" fill="none" stroke="var(--green)" stroke-width="2"/><circle cx="62" cy="58" r="5" fill="none" stroke="var(--green)" stroke-width="2"/><circle cx="75" cy="58" r="5" fill="none" stroke="var(--green)" stroke-width="2"/><path d="M30 82V68h12v14M43 82V68h12v14M56 82V68h12v14M69 82V68h12v14" fill="none" stroke="var(--green)" stroke-width="2"/></svg>
</div>

<!-- news -->
<div class="abs" style="left:0;top:2971px;width:1200px;height:639px;background:#fff">
  <div class="abs center" style="left:0;top:96px;width:1200px">
    <div class="eyebrow">News</div>
    <div class="h2" style="margin-top:6px">Our Latest News</div>
    <p class="body" style="margin-top:6px">Lorem ipsum dolor sit amet, consectetur adipiscing elit. Etiam<br>sollicitudin ante in purus viverra, vitae tempor lorem laoreet.</p>
  </div>
  <svg class="abs" style="left:92px;top:370px" width="26" height="40"><path d="M20 2L4 20l16 18" fill="none" stroke="#333" stroke-width="2"/></svg>
  <svg class="abs" style="left:1082px;top:370px" width="26" height="40"><path d="M6 2l16 18L6 38" fill="none" stroke="#333" stroke-width="2"/></svg>
</div>

<div class="abs" style="left:162px;top:3221px;width:274px;height:294px;background:#fff;box-shadow:0 2px 8px rgba(0,0,0,.15);border-radius:4px;overflow:hidden">
  <div role="img" aria-label="Photo of hands holding glasses over a desk with a coffee cup" style="height:144px;background:linear-gradient(135deg,#d8d8d6,#8a8a86)"></div>
  <div class="center" style="padding:10px 14px">
    <div style="font-size:13px;color:var(--green);font-weight:500">Lorem ipsum dolor sit amet, consectetur.</div>
    <div style="font-size:10px;margin-top:6px;color:#444">▣ May 18, 2021 &nbsp;&nbsp;&nbsp; ▭ 12 comments</div>
    <p style="font-size:10px;line-height:1.6;margin-top:6px">Lorem ipsum dolor sit amet, consectetur adipiscing elit. Etiam sollicitudin ante in purus viverra, vitae tempor lorem laoreet.</p>
    <div class="btn btn-green" style="margin-top:8px;width:90px;height:26px;line-height:26px;font-size:8px">Read more</div>
  </div>
</div>
<div class="abs" style="left:464px;top:3221px;width:274px;height:294px;background:#fff;box-shadow:0 2px 8px rgba(0,0,0,.15);border-radius:4px;overflow:hidden">
  <div role="img" aria-label="Photo of hands holding glasses over a desk with a coffee cup" style="height:144px;background:linear-gradient(135deg,#d8d8d6,#8a8a86)"></div>
  <div class="center" style="padding:10px 14px">
    <div style="font-size:13px;color:var(--green);font-weight:500">Lorem ipsum dolor sit amet, consectetur.</div>
    <div style="font-size:10px;margin-top:6px;color:#444">▣ May 18, 2021 &nbsp;&nbsp;&nbsp; ▭ 12 comments</div>
    <p style="font-size:10px;line-height:1.6;margin-top:6px">Lorem ipsum dolor sit amet, consectetur adipiscing elit. Etiam sollicitudin ante in purus viverra, vitae tempor lorem laoreet.</p>
    <div class="btn btn-green" style="margin-top:8px;width:90px;height:26px;line-height:26px;font-size:8px">Read more</div>
  </div>
</div>
<div class="abs" style="left:766px;top:3221px;width:274px;height:294px;background:#fff;box-shadow:0 2px 8px rgba(0,0,0,.15);border-radius:4px;overflow:hidden">
  <div role="img" aria-label="Photo of hands holding glasses over a desk with a coffee cup" style="height:144px;background:linear-gradient(135deg,#d8d8d6,#8a8a86)"></div>
  <div class="center" style="padding:10px 14px">
    <div style="font-size:13px;color:var(--green);font-weight:500">Lorem ipsum dolor sit amet, consectetur.</div>
    <div style="font-size:10px;margin-top:6px;color:#444">▣ May 18, 2021 &nbsp;&nbsp;&nbsp; ▭ 12 comments</div>
    <p style="font-size:10px;line-height:1.6;margin-top:6px">Lorem ipsum dolor sit amet, consectetur adipiscing elit. Etiam sollicitudin ante in purus viverra, vitae tempor lorem laoreet.</p>
    <div class="btn btn-green" style="margin-top:8px;width:90px;height:26px;line-height:26px;font-size:8px">Read more</div>
  </div>
</div>

<!-- testimonial + contact -->
<div class="abs" style="left:0;top:3610px;width:1200px;height:623px;background:var(--light)"></div>
<div class="abs" style="left:71px;top:3705px;width:514px;height:427px;background:var(--green);border-radius:4px;color:#fff">
  <div class="abs" style="left:32px;top:36px;width:44px;height:44px;border-radius:50%;background:#fff;color:var(--green);font-size:30px;text-align:center;line-height:52px;font-weight:600">❝</div>
  <p class="abs" style="left:32px;top:108px;width:450px;font-size:12px;line-height:2">Lorem ipsum dolor sit amet, consectetur adipiscing elit. Etiam sollicitudin ante in purus viverra, vitae tempor lorem laoreet. Vestibulum feugiat, ipsum a euismod finibus, massa nisl tristique lacus, eget pellentesque urna metus a turpis. Nullam eget feugiat enim. Sed id finibus felis. Quisque tincidunt nisl vel risus dapibus, sit amet aliquet justo elementum. Nam non lectus nisi. Nullam eget risus neque.</p>
  <div class="abs" role="img" aria-label="Small round portrait" style="left:32px;top:283px;width:28px;height:28px;border-radius:50%;background:#b9a89a"></div>
  <div class="abs" role="img" aria-label="Small round portrait" style="left:76px;top:283px;width:28px;height:28px;border-radius:50%;background:#b9a89a"></div>
  <div class="abs" role="img" aria-label="Round portrait of the quoted person" style="left:118px;top:274px;width:44px;height:44px;border-radius:50%;background:#3a3532;border:2px solid #fff"></div>
  <div class="abs" role="img" aria-label="Small round portrait" style="left:176px;top:283px;width:28px;height:28px;border-radius:50%;background:#b9a89a"></div>
  <div class="abs" role="img" aria-label="Small round portrait" style="left:218px;top:283px;width:28px;height:28px;border-radius:50%;background:#b9a89a"></div>
  <div class="abs" style="left:32px;top:340px;font-size:16px;font-weight:500">John Doe</div>
  <div class="abs" style="left:32px;top:368px;font-size:11px">CEO at (Company Name)</div>
  <svg class="abs" style="left:434px;top:350px" width="50" height="20"><path d="M10 4l-6 6 6 6M36 4l6 6-6 6" fill="none" stroke="#fff" stroke-width="1.5"/></svg>
</div>
<div class="abs" style="left:615px;top:3705px;width:516px;height:427px;background:#fff;border:1px solid var(--green);border-radius:4px">
  <div class="abs eyebrow" style="left:34px;top:42px">Contact us</div>
  <div class="abs h2" style="left:34px;top:60px">Get In Touch Now</div>
  <div class="abs" style="left:34px;top:126px;width:218px;height:32px;border:1px solid var(--green);border-radius:16px;font-size:10px;padding:9px 20px;color:#555">NAME</div>
  <div class="abs" style="left:264px;top:126px;width:218px;height:32px;border:1px solid var(--green);border-radius:16px;font-size:10px;padding:9px 20px;color:#555">EMAIL</div>
  <div class="abs" style="left:34px;top:180px;width:218px;height:32px;border:1px solid var(--green);border-radius:16px;font-size:10px;padding:9px 20px;color:#555">PHONE</div>
  <div class="abs" style="left:264px;top:180px;width:218px;height:32px;border:1px solid var(--green);border-radius:16px;font-size:10px;padding:9px 20px;color:#555">SUBJECT</div>
  <div class="abs" style="left:34px;top:232px;width:448px;height:84px;border:1px solid var(--green);border-radius:16px;font-size:10px;padding:10px 20px;color:#555">PHONE</div>
  <div class="abs btn btn-green" style="left:196px;top:358px;width:126px;height:32px;line-height:32px;font-size:9px">Send message</div>
</div>

<!-- call band -->
<div class="abs" style="left:0;top:4233px;width:1200px;height:186px;background:var(--ink)"></div>
<div class="abs" style="left:257px;top:4264px;width:686px;height:123px;background:var(--green);border-radius:14px;color:#fff">
  <svg class="abs" style="left:152px;top:30px" width="70" height="70" viewBox="0 0 70 70"><path d="M14 8c-6 4-9 10-6 18 6 16 20 30 36 36 8 3 14 0 18-6l-12-10-8 6C32 48 22 38 18 28l6-8z" fill="none" stroke="#2e3429" stroke-width="2.5" stroke-linejoin="round"/><path d="M40 12a18 18 0 0 1 18 18M40 20a10 10 0 0 1 10 10" fill="none" stroke="#2e3429" stroke-width="2.5"/></svg>
  <div class="abs" style="left:258px;top:34px;font-size:16px;letter-spacing:.3px">CALL TO ASK ANY QUESTION</div>
  <div class="abs" style="left:258px;top:58px;font-size:34px;font-weight:500">+41 79 512 80 47</div>
</div>

<!-- footer -->
<div class="abs" style="left:0;top:4419px;width:1200px;height:337px;background:#fff">
  <div class="abs logo" style="left:540px;top:42px;width:120px;text-align:center">tovrenu.ch</div>

  <div class="abs" style="left:162px;top:118px">
    <div style="font-size:14px;color:var(--green);font-weight:500">QUICK LINKS</div>
    <div style="font-size:11px;line-height:24px;margin-top:10px;color:#333">Home<br>About tovrenu<br>Courses<br>Unlock Your Potential<br>Contact</div>
  </div>
  <div class="abs" style="left:334px;top:118px">
    <div style="font-size:14px;color:var(--green);font-weight:500">ADDRESS</div>
    <div style="font-size:11px;line-height:24px;margin-top:10px;color:#333">
      <svg width="9" height="12" viewBox="0 0 10 13" style="vertical-align:-1px;margin-right:7px"><path d="M5 12S1 7 1 5a4 4 0 0 1 8 0c0 2-4 7-4 7z" fill="none" stroke="#333"/><circle cx="5" cy="5" r="1.5" fill="#333"/></svg>Lindenweg 18, CH-3930 Visp<br>
      <svg width="11" height="9" viewBox="0 0 12 10" style="vertical-align:0;margin-right:6px"><rect x="1" y="1" width="10" height="8" fill="none" stroke="#333"/><path d="M1 1l5 4 5-4" fill="none" stroke="#333"/></svg>info@tovrenu.ch<br>
      <svg width="8" height="12" viewBox="0 0 8 12" style="vertical-align:-1px;margin-right:9px"><rect x="1" y="1" width="6" height="10" rx="1" fill="none" stroke="#333"/></svg>+41 79 512 80 47
    </div>
  </div>
  <div class="abs" style="left:642px;top:118px">
    <div style="font-size:14px;color:var(--green);font-weight:500">COMPANY</div>
    <div style="font-size:11px;line-height:24px;margin-top:10px;color:#333">Home<br>Terms &amp; Conditions<br>Courses<br>Online Support<br>Contact</div>
  </div>
  <div class="abs" style="left:842px;top:118px;width:198px">
    <div style="font-size:14px;color:var(--green);font-weight:500">GET CONNECT</div>
    <p style="font-size:10.5px;line-height:2;margin-top:10px;color:#333;text-align:justify">Lorem ipsum dolor sit amet, consectetur adipiscing elit. Etiam sollicitudin ante in purus viverra, vitae tempor lorem laoreet. Vestibulum feugiat, ipsum a euismod finibus, massa nisl tristique lacus, eget pellentesque urna metus a turpis.</p>
    <div style="margin-top:12px;display:flex;gap:14px">
      <span style="width:20px;height:20px;border:1.5px solid var(--green);border-radius:50%"></span>
      <span style="width:20px;height:20px;border:1.5px solid var(--green);border-radius:50%"></span>
      <span style="width:20px;height:20px;border:1.5px solid var(--green);border-radius:50%"></span>
      <span style="width:20px;height:20px;border:1.5px solid var(--green);border-radius:50%"></span>
    </div>
  </div>
</div>
<div class="abs center" style="left:0;top:4756px;width:1200px;height:44px;background:var(--green);color:#fff;font-size:10px;line-height:44px">© 2021 TOVRENU ALL RIGHTS RESERVED</div>

</body>
</html>
```